Design Business Cards

MV construction is a construction company. business card should have:
- License #
- position
- name
- cell #
- office #
- website
any other ideas are welcome!

```html
<!DOCTYPE html>
<html lang="en">
<head>
<meta charset="utf-8">
<title>MV construction — Business Card</title>
<link rel="stylesheet" href="https://fonts.googleapis.com/css2?family=Open+Sans:wght@400;600;700&display=swap">
<style>
  :root{
    --bg:#e9e9ea;
    --card:#ffffff;
    --ink:#1c1c1c;
    --muted:#444444;
    --gold:#d6b928;
    --gold-dark:#b79a10;
    --gold-light:#eedc5c;
  }
  *{margin:0;padding:0;box-sizing:border-box}
  html,body{width:1200px;height:901px;overflow:hidden}
  body{background:var(--bg);font-family:"Open Sans",Arial,sans-serif;color:var(--ink);position:relative}
  .card{position:absolute;width:500px;height:286px;background:var(--card);border-radius:16px;overflow:hidden;box-shadow:0 6px 18px rgba(0,0,0,.15)}
  .card--front{left:70px;top:307px}
  .card--back{left:630px;top:307px}
  .card__swoosh{position:absolute;inset:0;width:100%;height:100%}
  .brand{position:absolute;display:flex;align-items:center;gap:10px;white-space:nowrap}
  .brand__mark{width:14px;height:14px;background:var(--gold);flex:none}
  .brand__name{font-weight:700;color:var(--ink);letter-spacing:1px;text-transform:uppercase}
  .card--front .brand{left:150px;top:44px}
  .card--front .brand__name{font-size:18px}
  .license{position:absolute;right:18px;top:143px;transform-origin:right top;transform:rotate(-90deg) translateX(50%);font-size:11px;font-weight:700;color:var(--ink);white-space:nowrap}
  .person{position:absolute;left:34px;top:124px}
  .person__name{font-size:17px;font-weight:700;color:var(--gold);line-height:22px}
  .person__role{font-size:13px;color:var(--muted);margin-bottom:8px;line-height:18px}
  .contact{list-style:none;font-size:11px;color:var(--muted);line-height:17px}
  .contact li{display:flex;align-items:center;gap:7px;white-space:nowrap}
  .contact svg{width:10px;height:10px;flex:none;fill:var(--gold)}
  .contact .contact__address{padding-left:17px}
  .card--back .brand{left:50%;top:112px;transform:translateX(-50%)}
  .card--back .brand__name{font-size:24px}
  .web-pill{position:absolute;left:50%;bottom:48px;transform:translateX(-50%);background:var(--ink);color:var(--gold);font-size:12px;font-weight:700;padding:4px 16px;border-radius:10px;white-space:nowrap}
</style>
</head>
<body>
  <section class="card card--front">
    <svg class="card__swoosh" viewBox="0 0 500 286" preserveAspectRatio="none" aria-hidden="true">
      <defs>
        <linearGradient id="goldBand" x1="0" y1="0" x2="1" y2="1">
          <stop offset="0" stop-color="#eedc5c"/>
          <stop offset=".5" stop-color="#d6b928"/>
          <stop offset="1" stop-color="#b79a10"/>
        </linearGradient>
      </defs>
      <path d="M300 286 C380 230 410 120 432 0 L500 0 L500 286 Z" fill="url(#goldBand)"/>
      <path d="M285 286 C365 228 394 120 414 0 L426 0 C404 122 376 230 300 286 Z" fill="#1c1c1c"/>
    </svg>
    <div class="brand"><span class="brand__mark"></span><span class="brand__name">MV construction</span></div>
    <div class="license">License No : 52013874</div>
    <div class="person">
      <div class="person__name">Daniel Reyes</div>
      <div class="person__role">Director</div>
      <ul class="contact">
        <li class="contact__address">14 Harlow Street</li>
        <li class="contact__address">Brookvale, New York</li>
        <li><svg viewBox="0 0 10 10"><path d="M2 0h2l1 3-1.5 1a6 6 0 0 0 2.5 2.5L7 5l3 1v2c0 1-1 2-2 2A8 8 0 0 1 0 2c0-1 1-2 2-2z"/></svg>03 555 018274</li>
        <li><svg viewBox="0 0 10 10"><rect x="0" y="2" width="10" height="7"/></svg>daniel@mvbuild.com</li>
        <li><svg viewBox="0 0 10 10"><circle cx="5" cy="5" r="5"/></svg>www.mvbuild.com</li>
      </ul>
    </div>
  </section>

  <section class="card card--back">
    <div class="brand"><span class="brand__mark"></span><span class="brand__name">MV construction</span></div>
    <div class="web-pill">www.mvbuild.com</div>
  </section>
</body>
</html>
```